Vorlen - Customer Experience Software Company Web Design

*****UPDATE*****
We've been getting a lot of corporate designs through. Unfortunately this is not what we are looking for. We would like our brand to be more approachable and for the look and feel to to be a bit more fun.
Also the best designs we have received so far have followed the "less is more" approach. Im hoping any news designs will take these aspects into account.
*****************

Background:

Vorlen is a Customer Experience Technology company. We equip business and technology teams with the frameworks, tools and services to help them create compelling experiences for their customers.

Our flagship product - Vorlen CX is an open-source customer experience application framework – it enables organisation to build highly differentiated business applications to deliver compelling experiences to your customers.

Vorlen CX is designed for innovators who understand that unlocking opportunity in today’s competitive marketplace is driven by delivering a better customer experience.

Task:

We are looking for a web design (we need PSD, no HTML/CSS) for our company site through which to launch our customer experience framework product. The site will be also used as a support site, so the functional aspect of the site is as important as the visual impact for sales.

In order to help us conceptualise ideas and content we have drafted a temporary website using a standard wordpress theme (please see details below). Now we have a general idea of our requirements we like we would like to take it to the next level and get some designs with that professional edge.

Our target market are Enterprise organisations - that is senior members of the business & technology teams (Business General Managers, CTO’s, CIO’s, and Senior Architects and Senior Developers). We want something clean & fresh which is DIFFERENT from the typical corporate technology websites out there. We would like to be seen as more approachable than most large technology companies.

Words we would like to use to describe the finished design:
• Clean (we’re thinking white background with one or two key colours)
• Fresh
• Light
• Modern
• Less is more
• Web 2.0
• Fun but professional (aimed at Enterprise/Large organisations)
• Bold, clear call to action – e.g. Live Demo & Download
• Readable (but Sans Serif)

As we’re a Customer Experience company, the usability of the site is critical. The site must be functional, intuitive & easy to navigate. We want to keep the number of user clicks to the bare minimum possible.

Other aspects, which we would like to incorporate into the site
• Home Page banner slider
• Client logon
• Newsletter sign up
• Social media links – Facebook, LinkedIn (for starters)
• Rich footer links

Some websites we like
• http://brightpanelworks.example - clean, light, modern & intuitive
• http://www.tamsoledrik.example - bold, clear messaging
• http://www.opengridhub.example/markup/emblem - punchy, colourful
• http://postwren.example/ - modern, clear messaging, colourful, rich footer area

Target Market(s)

Enterprise organisations - that is senior members of the business & technology teams (Business General Managers, CTO’s, CIO’s, Senior Devs)

Industry/Entity Type

Business

Requirements
Must have
• - Design Specs: Accepted file formats: During the design phase adobe PSD or JPEG are OK (if you need to upload files), but for the handover we'll need PSD only with all the original layers.
- The width needs to be a size that will work with every size computer screen
- Need to use cross-platform compatible font
- The graphic elements used for the design must be copyright free

Current test site
- URL http://vorlen.example/wp-admin
- username: artmarket
- password: artmarket

IMPORTANT NOTE REGARDING OUR CURRENT TEST SITE:

This is a very basic version of a site to help us generate requirements. This design is only a starting point/input and is not locked in stone i.e. we do not simply want this site simply tweaked around the edges.

We are looking for you to use all of your graphic design skills and experience to create a truly awesome site design!

```html
<!DOCTYPE html>
<html lang="en">
<head>
<meta charset="utf-8">
<title>Vorlen – Customer Experience Technology Company</title>
<link rel="stylesheet" href="https://fonts.googleapis.com/css2?family=Arimo:ital,wght@0,400;0,700;1,400;1,700&family=Cousine:ital@1&display=swap">
<style>
:root{
  --purple:#4b2459;
  --cyan:#5bc3e0;
  --cyan-dark:#3aa9c9;
  --link:#2f7fc4;
  --title:#2d5aa6;
  --ink:#333;
  --muted:#666;
  --header:#f5f5f5;
  --body:#e9e8e9;
  --panel:#fbfafb;
  --footer:#2b2a2b;
  --sans:"Arimo",Arial,sans-serif;
}
*{box-sizing:border-box;margin:0;padding:0}
html,body{width:1200px;height:900px;overflow:hidden;background:#fff}
body{position:relative;font-family:var(--sans);color:var(--ink)}
.abs{position:absolute}
.site{position:absolute;left:244px;top:10px;width:666px;height:888px;background:var(--body)}

/* header */
.header{left:0;top:0;width:666px;height:65px;background:var(--header)}
.brand{left:58px;top:10px;font:700 14px var(--sans);color:var(--purple);letter-spacing:.8px}
.tagline{left:18px;top:29px;font:7px var(--sans);color:#555;letter-spacing:.1px;white-space:nowrap}
.login-label{left:471px;top:14px;font:8px var(--sans);color:#333}
.field{top:12px;width:58px;height:12px;background:#fff;border-top:2px solid #999;font:6px var(--sans);color:#888;padding:1px 3px}
.signup{left:517px;top:28px;font:6px var(--sans);color:#777}
.signup b{color:#222;text-decoration:underline;font-weight:400;margin-left:3px}
.nav a{position:absolute;top:41px;height:19px;font:8.5px var(--sans);line-height:19px;color:#222;text-decoration:none}
.nav a.active{background:var(--purple);color:#fff;padding:0 6px}

/* slider */
.slider{left:0;top:65px;width:666px;height:168px;background:var(--purple)}
.slide{left:136px;top:15px;width:393px;height:130px;background:#fff;padding:3px;box-shadow:0 2px 6px rgba(0,0,0,.4)}
.slide-photo{width:100%;height:100%;background:linear-gradient(90deg,#c9ccd2 0%,#e6e4e2 45%,#eadbd0 75%,#f3f1ef 100%)}
.cta{top:100px;height:17px;padding:0 9px;border-radius:9px;font:700 7px var(--sans);line-height:17px;letter-spacing:.3px}
.cta-primary{left:152px;background:var(--cyan);color:#fff}
.cta-secondary{left:206px;background:#fff;color:var(--purple);border:1px solid var(--purple);line-height:15px}
.dot{top:154px;width:5px;height:5px;border-radius:50%;background:#fff}

/* main panel */
.panel{left:74px;top:241px;width:501px;height:234px;background:var(--panel)}
.h-section{font:700 6.5px var(--sans);color:#222}
.h-sub{font:5.5px var(--sans);color:var(--link)}
.copy{font:5px var(--sans);line-height:8.2px;color:#444}
.thumb{width:37px;height:37px;border:2px solid #fff;box-shadow:0 0 0 1px #999}
.divider{width:80px;height:6px}
.feature{font:700 5px var(--sans);line-height:8px;color:#222}
.feature span{font-weight:400}
.feature a{color:var(--link)}

/* services */
.card{top:487px;width:91px;height:78px;background:#fff;border-radius:3px;overflow:hidden}
.card-title{left:27px;top:10px;font:700 6.5px var(--sans);color:var(--title);letter-spacing:.2px}
.card-copy{left:5px;top:30px;width:80px;font:4.7px var(--sans);line-height:8.3px;color:#333}
.card-bar{left:0;bottom:0;width:91px;height:16px;background:var(--purple);color:#fff;font:4.8px var(--sans);line-height:16px;padding-left:6px}

/* blog and reviews */
.h-block{font:8px var(--sans);color:#222;letter-spacing:.3px}
.h-block-sub{font:4.8px var(--sans);color:#333}
.date{left:135px;width:26px;height:26px;border-radius:50%;background:var(--cyan);color:#fff;font:700 6px var(--sans);line-height:7px;text-align:center;padding-top:6px}
.date small{display:block;font-size:4px}
.post{left:169px;width:150px;font:5px var(--sans);line-height:8.2px;color:#444}
.post a{color:var(--link)}
.post-rule{left:135px;width:186px;height:1px;background:#888}
.quote{left:379px;width:148px;height:35px;background:#fff;border:1px solid #aaa;padding:5px 6px;font:italic 4.6px "Cousine",monospace;line-height:8px;color:#666}

/* tweet strip */
.strip{left:0;top:765px;width:666px;height:34px;background:#f7f7f7}
.tweet{left:156px;top:12px;font:italic 5px var(--sans);color:#666}
.tweet a{color:var(--link)}
.to-top{left:509px;top:787px;width:21px;height:21px;border-radius:50%;background:var(--cyan);color:#fff;font:700 4px var(--sans);text-align:center;padding-top:3px}

/* footer */
.footer{left:0;top:799px;width:666px;height:89px;background:var(--footer)}
.f-head{top:16px;font:700 5px var(--sans);color:#eee;letter-spacing:.2px}
.f-text{font:4px var(--sans);line-height:6px;color:#ccc}
.f-text a{color:var(--cyan)}
.f-pic{width:16px;height:16px;background:linear-gradient(135deg,#7a6f66,#cfc6bd)}
.f-brand{left:441px;top:13px;font:italic 10px var(--sans);color:#eee}
.social{top:866px;width:5px;height:5px;border-radius:50%;background:#888}
</style>
</head>
<body>
<div class="site">

  <header class="abs header">
    <div class="abs brand">VORLEN</div>
    <div class="abs tagline">CUSTOMER EXPERIENCE TECHNOLOGY COMPANY</div>
    <div class="abs login-label">Client Login</div>
    <div class="abs field" style="left:516px">user name</div>
    <div class="abs field" style="left:582px">password</div>
    <div class="abs signup">New User ? <b>Register Now</b></div>
    <nav class="nav">
      <a class="active" style="left:239px">Home</a>
      <a style="left:283px">Products</a>
      <a style="left:330px">Support</a>
      <a style="left:375px">Blog</a>
      <a style="left:405px">About</a>
    </nav>
  </header>

  <section class="abs slider">
    <svg class="abs" style="left:118px;top:72px" width="10" height="12" viewBox="0 0 10 12"><path d="M8 1L3 6l5 5" fill="none" stroke="#fff" stroke-width="2.5"/></svg>
    <div class="abs slide"><div class="slide-photo" role="img" aria-label="Smiling customer service agent in a bright office with colleagues behind"></div></div>
    <a class="abs cta cta-primary">LIVE DEMO</a>
    <a class="abs cta cta-secondary">DOWNLOAD</a>
    <svg class="abs" style="left:538px;top:72px" width="10" height="12" viewBox="0 0 10 12"><path d="M2 1l5 5-5 5" fill="none" stroke="#fff" stroke-width="2.5"/></svg>
    <span class="abs dot" style="left:320px;background:#111"></span>
    <span class="abs dot" style="left:329px"></span>
    <span class="abs dot" style="left:338px"></span>
  </section>

  <section class="abs panel">
    <div class="abs h-section" style="left:60px;top:10px">WHO WE ARE</div>
    <div class="abs h-sub" style="left:60px;top:19px">OUR TEAM</div>
    <p class="abs copy" style="left:60px;top:34px;width:150px">Duis sagittis dolor eget enim porttitor aliquam. Maecenas a nulla elit, vitae imperdiet sem.</p>
    <div class="abs thumb" role="img" aria-label="Team member photo" style="left:215px;top:12px;background:linear-gradient(135deg,#8a6a3a,#d8b070)"></div>
    <div class="abs thumb" role="img" aria-label="Team member photo" style="left:266px;top:12px;background:linear-gradient(135deg,#7a3b2a,#c98a5a)"></div>
    <div class="abs thumb" role="img" aria-label="Team meeting photo" style="left:316px;top:12px;background:linear-gradient(135deg,#5a3028,#d0b6a8)"></div>
    <div class="abs thumb" role="img" aria-label="Team at work photo" style="left:366px;top:12px;background:linear-gradient(135deg,#4a4a5a,#c0c4cc)"></div>
    <div class="abs thumb" role="img" aria-label="Team member photo" style="left:417px;top:12px;background:linear-gradient(135deg,#b08a70,#eae0d6)"></div>

    <svg class="abs divider" style="left:219px;top:68px" viewBox="0 0 80 6"><path d="M0 3h33M47 3h33" stroke="#888" stroke-width=".8"/><circle cx="36" cy="3" r="1" fill="#888"/><circle cx="40" cy="3" r="1.6" fill="var(--purple)"/><circle cx="44" cy="3" r="1" fill="#888"/></svg>

    <div class="abs h-section" style="left:60px;top:90px">WHAT WE DO</div>
    <div class="abs h-sub" style="left:60px;top:99px">WE BUILD QUALITY PRODUCTS</div>
    <p class="abs copy" style="left:60px;top:115px;width:158px">Praesent mattis, dui eget mattis lacinia, nibh dui lobortis est, a dapibus nunc mi sed nisl. Cras leo risus, consequat nec lacinia at, mattis at risus. Sed a rhoncus quam.</p>
    <p class="abs copy" style="left:60px;top:148px;width:158px">Praesent mattis, dui eget mattis lacinia, nibh dui lobortis est, a dapibus nunc mi sed nisl. Cras leo risus, consequat nec lacinia at, mattis at risus. Sed a rhoncus quam, erat ridiculus mus. Cras hendrerit dui mollis tortor aliquam vestibulum. In placerat, justo sit ame</p>
    <svg class="abs" style="left:60px;top:191px" width="17" height="17" viewBox="0 0 17 17"><circle cx="8.5" cy="8.5" r="8" fill="#3f83c6"/><path d="M3 8.5h11M8.5 1v15M4.5 4c3 2 5 2 8 0M4.5 13c3-2 5-2 8 0" stroke="#cfe3f5" stroke-width=".7" fill="none"/></svg>
    <div class="abs feature" style="left:81px;top:193px">FREE ON-LINE SUPPORT<br><span>Talk Us On <a>Chatterly</a> or <a>Pingo</a></span></div>
    <svg class="abs" style="left:157px;top:188px" width="18" height="20" viewBox="0 0 18 20"><circle cx="9" cy="11" r="7.5" fill="#fff" stroke="#3f83c6" stroke-width="1.5"/><rect x="7" y="1" width="4" height="2.5" fill="#3f83c6"/><path d="M9 11V6.5M9 11l3 2" stroke="#333" stroke-width=".9"/></svg>
    <div class="abs feature" style="left:178px;top:192px">WE ON-LINE 24 HOURS<br><span><a>Call Now</a></span></div>

    <div class="abs h-section" style="left:264px;top:90px">OUR WORK</div>
    <div class="abs h-sub" style="left:264px;top:99px">OUR LATEST PROJECTS</div>
    <svg class="abs" style="left:444px;top:93px" width="14" height="8" viewBox="0 0 14 8"><path d="M4 1L1 4l3 3M10 1l3 3-3 3" fill="none" stroke="#444" stroke-width="1"/></svg>
    <div class="abs thumb" role="img" aria-label="Project photo: hand writing on documents" style="left:266px;top:117px;background:linear-gradient(135deg,#e8e8ea,#7a7f8a)"></div>
    <div class="abs thumb" role="img" aria-label="Project photo: person at a laptop" style="left:316px;top:117px;background:linear-gradient(135deg,#9ab6d6,#e9edf2)"></div>
    <div class="abs thumb" role="img" aria-label="Project photo: people at a whiteboard" style="left:367px;top:117px;background:linear-gradient(135deg,#d6d0c8,#8a7c70)"></div>
    <div class="abs thumb" role="img" aria-label="Project photo: hands on a keyboard" style="left:417px;top:117px;background:linear-gradient(135deg,#f0f0f0,#5a5a5a)"></div>
    <div class="abs thumb" role="img" aria-label="Project photo: modern building interior" style="left:266px;top:168px;background:linear-gradient(135deg,#2a4a8a,#8ab0e0)"></div>
    <div class="abs thumb" role="img" aria-label="Project photo: office workspace" style="left:316px;top:168px;background:linear-gradient(180deg,#e0e2e0,#8c9a6a)"></div>
    <div class="abs thumb" role="img" aria-label="Project photo: conference room" style="left:367px;top:168px;background:linear-gradient(180deg,#3a5a9a,#c0c8d8)"></div>
    <div class="abs thumb" role="img" aria-label="Project photo: open office" style="left:417px;top:168px;background:linear-gradient(180deg,#dcdedc,#8c9a6a)"></div>

    <svg class="abs divider" style="left:219px;top:223px" viewBox="0 0 80 6"><path d="M0 3h33M47 3h33" stroke="#888" stroke-width=".8"/><circle cx="36" cy="3" r="1" fill="#888"/><circle cx="40" cy="3" r="1.6" fill="var(--purple)"/><circle cx="44" cy="3" r="1" fill="#888"/></svg>
  </section>

  <section>
    <article class="abs card" style="left:136px">
      <svg class="abs" style="left:4px;top:5px" width="18" height="16" viewBox="0 0 18 16"><path d="M9 1L17 15H1z" fill="#e84a8a"/><path d="M9 1L13 8H5z" fill="#f6c23a"/><path d="M5 8L9 15H1z" fill="#3fa4dc"/><path d="M13 8L17 15H9z" fill="#5cc05a"/></svg>
      <div class="abs card-title">WEB DESIGN</div>
      <p class="abs card-copy">Lorem ipsum dolor sit amet, consectetur adipiscing elit. Morbi sit amet velit non neque eleifend dapibus</p>
      <div class="abs card-bar">Learn More →</div>
    </article>
    <article class="abs card" style="left:237px">
      <svg class="abs" style="left:4px;top:4px" width="18" height="16" viewBox="0 0 18 16"><circle cx="9" cy="8" r="5" fill="none" stroke="#e8733a" stroke-width="3" stroke-dasharray="3 2"/></svg>
      <div class="abs card-title">DEVELOPMENT</div>
      <p class="abs card-copy">Lorem ipsum dolor sit amet, consectetur adipiscing elit. Morbi sit amet velit non neque eleifend dapibus</p>
      <div class="abs card-bar">Learn More →</div>
    </article>
    <article class="abs card" style="left:338px">
      <svg class="abs" style="left:4px;top:2px" width="18" height="18" viewBox="0 0 18 18"><circle cx="9" cy="6" r="4" fill="#8a6a50"/><path d="M2 18c0-6 14-6 14 0z" fill="#555"/></svg>
      <div class="abs card-title">STRATEGY</div>
      <p class="abs card-copy">Lorem ipsum dolor sit amet, consectetur adipiscing elit. Morbi sit amet velit non neque eleifend dapibus</p>
      <div class="abs card-bar">Learn More →</div>
    </article>
    <article class="abs card" style="left:439px">
      <svg class="abs" style="left:4px;top:4px" width="18" height="16" viewBox="0 0 18 16"><circle cx="9" cy="8" r="6" fill="none" stroke="#d93a3a" stroke-width="3"/><circle cx="9" cy="8" r="6" fill="none" stroke="#fff" stroke-width="3" stroke-dasharray="3 6.4"/></svg>
      <div class="abs card-title">SUPPORT</div>
      <p class="abs card-copy">Lorem ipsum dolor sit amet, consectetur adipiscing elit. Morbi sit amet velit non neque eleifend dapibus</p>
      <div class="abs card-bar">Learn More →</div>
    </article>
    <svg class="abs divider" style="left:293px;top:575px" viewBox="0 0 80 6"><path d="M0 3h33M47 3h33" stroke="#888" stroke-width=".8"/><circle cx="36" cy="3" r="1" fill="#888"/><circle cx="40" cy="3" r="1.6" fill="var(--purple)"/><circle cx="44" cy="3" r="1" fill="#888"/></svg>
  </section>

  <section>
    <div class="abs h-block" style="left:134px;top:604px">RECENT BLOG POSTS</div>
    <div class="abs h-block-sub" style="left:134px;top:614px">FROM OUR BLOG</div>

    <div class="abs date" style="top:630px">JUN<small>09</small></div>
    <p class="abs post" style="top:630px">Lorem ipsum dolor sit amet, consectetur adipiscing elit. Morbi sit amet velit non neque eleifend dapibus.<br>by <a>Teo</a> / <a>4 hours ago</a> / in <a>Unitedstates</a></p>
    <div class="abs post-rule" style="top:663px"></div>

    <div class="abs date" style="top:672px">APRIL<small>12</small></div>
    <p class="abs post" style="top:672px">Lorem ipsum dolor sit amet, consectetur adipiscing elit. Morbi sit amet velit non neque eleifend dapibus.<br>by <a>Teo</a> / <a>4 hours ago</a> / in <a>Unitedstates</a></p>
    <div class="abs post-rule" style="top:706px"></div>

    <div class="abs date" style="top:714px">JUN<small>09</small></div>
    <p class="abs post" style="top:714px">Lorem ipsum dolor sit amet, consectetur adipiscing elit. Morbi sit amet velit non neque eleifend dapibus.<br>by <a>Teo</a> / <a>4 hours ago</a> / in <a>Unitedstates</a></p>
    <div class="abs post-rule" style="top:748px"></div>

    <div class="abs h-block" style="left:337px;top:604px">WHAT OUR CLIENT SAYS</div>
    <div class="abs h-block-sub" style="left:337px;top:614px">MEET REVIEWS</div>
    <blockquote class="abs quote" style="top:628px">“ Duis sagittis dolor eget enim porttitor aliqua Praesent hendrerit, orci et ornare semper, lectus justo dictum ante</blockquote>
    <blockquote class="abs quote" style="top:670px">“ Duis sagittis dolor eget enim porttitor aliqua Praesent hendrerit, orci et ornare semper, lectus justo dictum ante</blockquote>
    <blockquote class="abs quote" style="top:712px">“ Duis sagittis dolor eget enim porttitor aliqua Praesent hendrerit, orci et ornare semper, lectus justo dictum ante</blockquote>
  </section>

  <div class="abs strip">
    <div class="abs" role="img" aria-label="Small bird mascot illustration" style="left:132px;top:6px;width:16px;height:18px;border-radius:50%;background:linear-gradient(135deg,#6a4a9a,#3a2a5a)"></div>
    <p class="abs tweet"><a>about a minute ago</a>&nbsp; Lorem ipsum dolor sit demonstrate. &nbsp;dui lobortis est, a dapibus nunc mi sed nis</p>
  </div>

  <footer class="abs footer">
    <div class="abs f-head" style="left:135px">RECENT COMMENTS</div>
    <div class="abs f-pic" role="img" aria-label="Commenter avatar" style="left:135px;top:31px"></div>
    <p class="abs f-text" style="left:156px;top:32px">Lorem ipsum dolor sit amet...<br><a>read more</a></p>
    <div class="abs f-pic" role="img" aria-label="Commenter avatar" style="left:135px;top:53px"></div>
    <p class="abs f-text" style="left:156px;top:54px">Lorem ipsum dolor sit amet...<br><a>read more</a></p>

    <div class="abs f-head" style="left:237px">FROM SNAPHIVE</div>
    <div class="abs f-pic" role="img" aria-label="Gallery photo" style="left:237px;top:31px"></div>
    <div class="abs f-pic" role="img" aria-label="Gallery photo" style="left:258px;top:31px"></div>
    <div class="abs f-pic" role="img" aria-label="Gallery photo" style="left:280px;top:31px;background:linear-gradient(135deg,#eee,#999)"></div>
    <div class="abs f-pic" role="img" aria-label="Gallery photo" style="left:301px;top:31px;background:linear-gradient(135deg,#eee,#777)"></div>
    <div class="abs f-pic" role="img" aria-label="Gallery photo" style="left:237px;top:53px"></div>
    <div class="abs f-pic" role="img" aria-label="Gallery photo" style="left:258px;top:53px"></div>
    <div class="abs f-pic" role="img" aria-label="Gallery photo" style="left:280px;top:53px;background:linear-gradient(135deg,#aaa,#555)"></div>
    <div class="abs f-pic" role="img" aria-label="Gallery photo" style="left:301px;top:53px;background:linear-gradient(135deg,#ddd,#888)"></div>

    <div class="abs f-head" style="left:339px">SUBSCRIBE FOR NEWSLETTER</div>
    <p class="abs f-text" style="left:339px;top:32px;width:84px">Quisque gravida leo ac lectus gravida posuere vel in leo.</p>
    <div class="abs f-text" style="left:339px;top:56px;width:80px;border-bottom:1px solid #777;padding-bottom:1px">Type email...</div>
    <svg class="abs" style="left:411px;top:55px" width="9" height="7" viewBox="0 0 9 7"><rect width="9" height="7" fill="#ddd"/><path d="M0 0l4.5 4L9 0" stroke="#555" stroke-width=".7" fill="none"/></svg>

    <div class="abs f-brand">vorlen</div>
    <p class="abs f-text" style="left:441px;top:33px;color:#ddd">Copyright 2011. All Rights Reserved</p>
    <div class="abs f-head" style="left:441px;top:56px">STAY IN TOUCH</div>
  </footer>
  <span class="abs social" style="left:443px"></span>
  <span class="abs social" style="left:450px"></span>
  <span class="abs social" style="left:457px"></span>
  <span class="abs social" style="left:464px"></span>
  <span class="abs social" style="left:471px"></span>

  <div class="abs to-top">
    <svg width="8" height="5" viewBox="0 0 8 5" style="display:block;margin:1px auto 0"><path d="M1 4l3-3 3 3" fill="none" stroke="#fff" stroke-width="1.4"/></svg>TOP
  </div>
</div>
</body>
</html>
```